Flyer to Promote Membership in a Trade Association

UPDATE: I am looking for something modern and clean. NO CLIP ART. Not flashy. Just professional and modern. For everyone looking at our current flyer, we don't like it. That's why we aer looking for a new one. So please don't replicate it or use it as inspiration.

I need a flyer to promote membership in the Durable Residence Backers League. It can (probably should) be 2-sided. The content is attached as well as our logo and brand guidelines.

```html
<!DOCTYPE html>
<html lang="en">
<head>
<meta charset="utf-8">
<title>Durable Residence Backers League – Membership</title>
<link href="https://fonts.googleapis.com/css2?family=Bitter:wght@400;500;600;700&family=Lato:wght@400;700&display=swap" rel="stylesheet">
<style>
  :root {
    --orange: #ef7622;
    --ink: #111111;
    --grey: #6d7074;
    --paper: #ffffff;
    --photo-light: #e9e7e2;
    --photo-mid: #b8ab8c;
    --photo-dark: #2b2f38;
  }
  * { margin: 0; padding: 0; box-sizing: border-box; }
  html, body { width: 848px; height: 1200px; overflow: hidden; background: var(--paper); }
  .flyer { position: relative; width: 848px; height: 1200px; overflow: hidden; background: var(--paper); font-family: "Lato", sans-serif; color: var(--ink); }
  .hero-shapes { position: absolute; inset: 0; width: 848px; height: 1200px; }

  .brand { position: absolute; left: 48px; top: 52px; display: flex; align-items: center; gap: 12px; }
  .brand-mark { width: 40px; height: 40px; background: var(--orange); }
  .brand-name { font-family: "Bitter", serif; font-weight: 600; font-size: 13px; line-height: 14px; letter-spacing: 0.6px; text-transform: uppercase; color: var(--grey); width: 130px; }

  .headline { position: absolute; left: 47px; top: 556px; font-family: "Bitter", serif; font-weight: 600; font-size: 58px; line-height: 64px; color: var(--orange); }
  .subhead { position: absolute; left: 48px; top: 619px; font-family: "Bitter", serif; font-weight: 600; font-size: 33px; line-height: 45.5px; color: var(--ink); white-space: nowrap; }
  .intro { position: absolute; left: 48px; top: 795px; font-size: 16.5px; line-height: 25.7px; color: var(--ink); white-space: nowrap; }

  .stat { position: absolute; top: 977px; width: 140px; text-align: center; }
  .stat-years { left: 54px; }
  .stat-firms { left: 176px; }
  .stat-people { left: 317px; }
  .stat-icon { width: 50px; height: 50px; display: block; margin: 0 auto; }
  .stat-number { font-family: "Bitter", serif; font-weight: 500; font-size: 24px; line-height: 30px; margin-top: 6px; }
  .stat-label { font-family: "Bitter", serif; font-weight: 400; font-size: 11.5px; line-height: 17px; letter-spacing: 0.3px; text-transform: uppercase; margin-top: 2px; }

  .members { position: absolute; left: 536px; top: 638px; width: 300px; }
  .members-title { font-family: "Bitter", serif; font-weight: 600; font-size: 27px; line-height: 32px; color: var(--orange); }
  .members-rule { width: 86px; height: 3px; background: var(--ink); margin-top: 4px; }
  .activity-list { list-style: none; margin-top: 18px; }
  .activity { display: flex; align-items: flex-start; height: 68.4px; }
  .activity-icon { width: 40px; height: 40px; margin-right: 18px; margin-top: 4px; flex: none; }
  .activity-name { font-weight: 700; font-size: 19px; line-height: 22px; }
  .activity-detail { font-size: 16.5px; line-height: 22px; }
  .members-note { position: absolute; left: 536px; top: 1028px; font-size: 16.5px; line-height: 25.5px; white-space: nowrap; }

  .footer-band { position: absolute; left: 0; top: 1118px; width: 848px; height: 82px; background: var(--orange); }
</style>
</head>
<body>
<main class="flyer">
  <svg class="hero-shapes" viewBox="0 0 848 1200">
    <defs>
      <linearGradient id="deskScene" x1="0" y1="0" x2="1" y2="1">
        <stop offset="0" stop-color="#2b2f38"/>
        <stop offset="0.45" stop-color="#b8ab8c"/>
        <stop offset="1" stop-color="#e9e7e2"/>
      </linearGradient>
    </defs>
    <path fill="#ef7622" d="M520,0 L848,0 L848,502 L652,600 Q600,628 548,598 L0,277 L0,150 L92,203 Q135,228 178,203 Z"/>
    <path fill="url(#deskScene)" role="img" aria-label="Investor in a suit inspecting a model house with a magnifying glass beside stacks of coins on banknotes" d="M578,0 L848,0 L848,428 L662,540 Q617,566 572,541 L0,235 L0,172 L92,224 Q135,248 180,222 Z"/>
  </svg>

  <div class="brand">
    <span class="brand-mark"></span>
    <span class="brand-name">Durable Residence Backers League</span>
  </div>

  <h1 class="headline">Where LIHTC</h1>
  <p class="subhead">Investing Excellence Begins<br>The Only Community Built<br>Exclusively for Investors</p>

  <p class="intro">DRBL is where federal housing credit investors<br>connect, learn, and lead. We are the only organization<br>solely dedicated to LIHTC investors - giving you a<br>trusted peer network, industry-setting standards, and<br>the insights to stay informed.</p>

  <div class="stat stat-years">
    <svg class="stat-icon" viewBox="0 0 52 52" fill="none" stroke="#ef7622">
      <path d="M44 20 A20 20 0 1 0 40 40" stroke-width="6" stroke-linecap="round"/>
      <path d="M44 28 L44 30 M41 37 L40 38" stroke-width="4" stroke-linecap="round"/>
      <path d="M26 14 V27 L34 33" stroke-width="4" stroke-linecap="round"/>
    </svg>
    <div class="stat-number">30</div>
    <div class="stat-label">Years<br>of Impact</div>
  </div>
  <div class="stat stat-firms">
    <svg class="stat-icon" viewBox="0 0 52 52" fill="#ef7622">
      <circle cx="20" cy="14" r="9"/>
      <path d="M4 46 Q4 27 20 27 Q28 27 32 32 L32 46 Z"/>
      <path d="M42 2 L48 9 H44 V20 H40 V9 H36 Z"/>
      <text x="41" y="47" font-family="Lato, sans-serif" font-weight="700" font-size="22" text-anchor="middle">$</text>
    </svg>
    <div class="stat-number">60+</div>
    <div class="stat-label">Investor<br>Firms</div>
  </div>
  <div class="stat stat-people">
    <svg class="stat-icon" viewBox="0 0 52 52" fill="#ef7622">
      <rect x="2" y="44" width="48" height="4"/>
      <rect x="5" y="28" width="9" height="16"/>
      <rect x="15" y="18" width="8" height="26"/>
      <rect x="24" y="12" width="10" height="32"/>
      <rect x="35" y="24" width="12" height="20"/>
      <rect x="18" y="12" width="2" height="6"/>
    </svg>
    <div class="stat-number">1,000+</div>
    <div class="stat-label">Industry<br>Professionals</div>
  </div>

  <section class="members">
    <h2 class="members-title">What Members Do</h2>
    <div class="members-rule"></div>
    <ul class="activity-list">
      <li class="activity">
        <svg class="activity-icon" viewBox="0 0 40 40" fill="#ef7622">
          <circle cx="20" cy="6" r="4.5"/><path d="M13 19 Q13 11 20 11 Q27 11 27 19 Z"/>
          <circle cx="7" cy="26" r="4.5"/><path d="M0 39 Q0 31 7 31 Q14 31 14 39 Z"/>
          <circle cx="33" cy="26" r="4.5"/><path d="M26 39 Q26 31 33 31 Q40 31 40 39 Z"/>
          <path d="M15 35 H25 M17 21 L12 28 M23 21 L28 28" stroke="#ef7622" stroke-width="1.5"/>
        </svg>
        <div><div class="activity-name">Network:</div><div class="activity-detail">Peer Groups &amp; Forums</div></div>
      </li>
      <li class="activity">
        <svg class="activity-icon" viewBox="0 0 40 40" fill="#ef7622">
          <path d="M0 14 L20 7 L40 14 L20 21 Z"/>
          <path d="M9 19 V28 Q20 33 31 28 V19 L20 23 Z"/>
          <rect x="36" y="14" width="2" height="12"/>
        </svg>
        <div><div class="activity-name">Learn:</div><div class="activity-detail">Conferences &amp; Webinars</div></div>
      </li>
      <li class="activity">
        <svg class="activity-icon" viewBox="0 0 40 40" fill="#ef7622">
          <path d="M4 4 H24 Q28 4 28 8 V20 Q28 24 24 24 H12 L5 30 V24 Q1 24 1 20 V8 Q1 4 4 4 Z"/>
          <path d="M30 14 H34 Q38 14 38 18 V28 Q38 31 35 31 V37 L29 31 H20 Q16 31 16 27 H25 Q31 27 31 21 Z"/>
        </svg>
        <div><div class="activity-name">Share:</div><div class="activity-detail">Candid Investor Exchange</div></div>
      </li>
      <li class="activity">
        <svg class="activity-icon" viewBox="0 0 40 40" fill="#ef7622">
          <rect x="4" y="28" width="5" height="10"/><rect x="13" y="24" width="5" height="14"/>
          <rect x="22" y="27" width="5" height="11"/><rect x="31" y="18" width="5" height="20"/>
          <path d="M5 20 L15 12 L24 18 L35 5" fill="none" stroke="#ef7622" stroke-width="2"/>
          <circle cx="5" cy="20" r="2.5"/><circle cx="15" cy="12" r="2.5"/><circle cx="24" cy="18" r="2.5"/><circle cx="35" cy="5" r="2.5"/>
        </svg>
        <div><div class="activity-name">Shape:</div><div class="activity-detail">Standards &amp; Best Practices</div></div>
      </li>
      <li class="activity">
        <svg class="activity-icon" viewBox="0 0 40 40" fill="#ef7622">
          <path d="M19 36 V18" stroke="#ef7622" stroke-width="3" fill="none"/>
          <path d="M19 20 Q8 20 6 8 Q17 8 19 20 Z"/>
          <path d="M19 24 Q22 12 34 12 Q32 24 19 24 Z"/>
          <path d="M8 38 Q8 32 19 32 Q30 32 30 38 Z"/>
        </svg>
        <div><div class="activity-name">Grow:</div><div class="activity-detail">Professional Development</div></div>
      </li>
    </ul>
  </section>

  <p class="members-note">One membership, unlimited access.<br>Your entire team can participate in<br>DRBL activities</p>

  <div class="footer-band"></div>
</main>
</body>
</html>
```